Eco friendly Swedish beauty products sold in aluminum bottles - label design needed

We need help in designing a series of stick on labels for 80 ml (2.7 fl. oz.) aluminum bottles containing beauty products such as soaps, shampoo etc. The diameter of the bottle is 36 mm and the body of the bottles measures approx. 106 mm.
It is important for us that the label has a simplistic and clean feel with few colors (and the right ones!) and that the label helps amplify this product being both better and a more sustainable alternative to many of our plastic bottle competitors. The design and label should communicate the feel of an Eco-friendly, sustainable and modern brand of high quality - and with a Swedish concept.
We are using Montserrat font in our materials. Find attached information of preferred colors, the bottles and one example of our logotype. I am also available on e-mail should further information be needed.

Looking forward and very excited to receive your suggestions.
Note that we are expecting to start selling a series of approximately 10 different products where I will need one "master design" and then only smaller changes for each of the different products.

Target Market(s)

People whom are aware and not only look at price tag. Private and commercial market.

Industry/Entity Type

Beauty

Font styles to use
Other font styles liked:
• Montserrat

Requirements
Must have
• It must give the feel of being both better and a more sustainable alternative to many of our plastic bottle competitors.
Nice to have
• Simplistic. Clean. Clear.
Should not have
• Wrong colors, too complex designs.

```html
<!DOCTYPE html>
<html lang="en">
<head>
<meta charset="utf-8">
<title>Nordlin Care – Label Series</title>
<link href="https://fonts.googleapis.com/css2?family=Montserrat:wght@300;400;500&display=swap" rel="stylesheet">
<style>
  :root {
    --ink: #1d1d1b;
    --paper: #ffffff;
    --stage: #f1f1f1;
    --moss: #6b7d3e;
    --rust: #9c432c;
    --sand: #e1b897;
    --amber: #a86525;
  }
  html, body {
    margin: 0;
    padding: 0;
    width: 1200px;
    height: 849px;
    overflow: hidden;
    background: var(--paper);
    font-family: "Montserrat", sans-serif;
  }
  .sheet {
    position: relative;
    width: 1200px;
    height: 849px;
  }
  .stage {
    position: absolute;
    left: 252px;
    top: 90px;
    width: 685px;
    height: 660px;
    background: var(--stage);
  }
  .brand-header {
    position: absolute;
    left: 300px;
    top: 130px;
    display: flex;
    align-items: center;
    gap: 8px;
    color: var(--ink);
  }
  .brand-header .mark {
    width: 10px;
    height: 10px;
    border-radius: 50%;
    background: var(--ink);
  }
  .brand-header .name {
    font-size: 15px;
    font-weight: 400;
    letter-spacing: 0.5px;
    line-height: 1;
  }
  .brand-header .origin {
    display: block;
    font-size: 5px;
    letter-spacing: 1.2px;
    text-align: right;
    margin-top: 3px;
  }
  .print-note {
    position: absolute;
    left: 493px;
    top: 135px;
    font-size: 15px;
    font-weight: 300;
    color: var(--ink);
  }
  .label {
    position: absolute;
    width: 80px;
    height: 300px;
  }
  .label .band {
    position: absolute;
    left: 0;
    width: 27px;
    background: var(--tone);
    color: var(--paper);
    writing-mode: vertical-rl;
    font-size: 13px;
    font-weight: 300;
    padding-top: 8px;
    box-sizing: border-box;
    display: flex;
    align-items: center;
    white-space: nowrap;
  }
  .label .band .volume {
    margin-top: auto;
    margin-bottom: 8px;
    font-size: 8px;
    padding-top: 6px;
    border-top: 1px solid var(--paper);
  }
  .label .brand {
    position: absolute;
    left: 31px;
    writing-mode: vertical-rl;
    color: var(--tone);
    font-size: 15px;
    font-weight: 400;
    letter-spacing: 0.5px;
    white-space: nowrap;
  }
  .label .brand .origin {
    display: block;
    font-size: 4.5px;
    letter-spacing: 1.2px;
    text-align: right;
  }
  .label .brand-dot {
    position: absolute;
    left: 38px;
    width: 8px;
    height: 8px;
    border-radius: 50%;
    background: var(--tone);
  }
  .label .swatch {
    position: absolute;
    width: 32px;
    height: 32px;
    border-radius: 50%;
    background: var(--tone);
  }
  .conditioner { --tone: var(--moss); left: 373px; top: 380px; }
  .shampoo { --tone: var(--rust); left: 477px; top: 395px; }
  .sanitizer { --tone: var(--sand); left: 645px; top: 385px; }
  .soap { --tone: var(--amber); left: 750px; top: 405px; }
</style>
</head>
<body>
<div class="sheet">
  <div class="stage"></div>

  <div class="brand-header">
    <span class="mark"></span>
    <span class="name">NORDLIN CARE<span class="origin">SWEDEN</span></span>
  </div>
  <div class="print-note">1C Print</div>

  <div class="label conditioner">
    <span class="brand-dot" style="top:8px"></span>
    <div class="band" style="top:27px;height:241px">Conditioner &amp; Body Lotion<span class="volume">80ml</span></div>
    <div class="brand" style="top:22px">NORDLIN CARE<span class="origin">SWEDEN</span></div>
    <span class="swatch" style="left:-2px;top:282px"></span>
  </div>

  <div class="label shampoo">
    <span class="brand-dot" style="top:0"></span>
    <div class="band" style="top:29px;height:243px">Hair Shampoo</div>
    <div class="brand" style="top:18px">NORDLIN CARE<span class="origin">SWEDEN</span></div>
    <span class="swatch" style="left:20px;top:283px"></span>
  </div>

  <div class="label sanitizer">
    <span class="brand-dot" style="top:5px"></span>
    <div class="band" style="top:27px;height:243px">Hand Sanitizer<span class="volume">80ml</span></div>
    <div class="brand" style="top:22px">NORDLIN CARE<span class="origin">SWEDEN</span></div>
    <span class="swatch" style="left:21px;top:283px"></span>
  </div>

  <div class="label soap">
    <span class="brand-dot" style="top:0"></span>
    <div class="band" style="top:27px;height:242px">Body soap</div>
    <div class="brand" style="top:18px">NORDLIN CARE<span class="origin">SWEDEN</span></div>
    <span class="swatch" style="left:20px;top:284px"></span>
  </div>
</div>
</body>
</html>
```